Brindlemoor Realty information card

We need a 5x7 two-sided card to hand out at open houses and provide to our charitable partners for distribution. We are a local real estate group looking to add a "give back" component to our business. We are located in a coastal community and would like to incorporate that feel into our design. We are giving clients who use us the ability to designate 1 out of the 10 charitable organizations we partner with - and we will make a donation to that organization.

We included the 10 partner logos below - we envision them pretty small. Also included 2 photos of the "Brindlemoor" and our logo. Have fun.
Updates

Project Deadline Extended
Reason: We're out of town until Wednesday, May 17th.

Target Market(s)

home buyers & sellers

Industry/Entity Type

Real Estate

Font styles to use
Serif
Sans Serif

Colors

Designer to choose colors to be used in the design.

Requirements
Must have
• slogan & tagline - see attached text file
• Brindlemoor photo
Nice to have
• partner logos - small - maybe in circles?

```html
<!DOCTYPE html>
<html lang="en">
<head>
<meta charset="utf-8">
<title>Brindlemoor Realty – Information Card</title>
<link rel="stylesheet" href="https://fonts.googleapis.com/css2?family=Lobster+Two:ital,wght@1,700&family=Source+Sans+3:ital,wght@0,400;0,600;0,700;1,600&display=block">
<style>
  :root {
    --navy: #1c3a72;
    --sky-blue: #7fa0cf;
    --white: #ffffff;
    --page: #e9e9e7;
    --ink-grey: #5a5f6a;
    --badge-ring: #c9ced8;
  }
  * { box-sizing: border-box; margin: 0; padding: 0; }
  html, body {
    width: 907px; height: 1200px; overflow: hidden;
    background: var(--page);
    font-family: "Source Sans 3", "Helvetica Neue", Arial, sans-serif;
  }
  .card {
    position: absolute; left: 91px; width: 703px; height: 503px;
    background: var(--white); overflow: hidden;
    box-shadow: 0 2px 8px rgba(0,0,0,0.18);
  }
  .card--front { top: 70px; }
  .card--back { top: 629px; }

  .card__header {
    position: absolute; left: 0; top: 0; width: 100%; height: 67px;
    background: var(--navy);
    display: flex; align-items: center;
  }
  .brand {
    width: 150px; text-align: center;
    color: var(--white); font-weight: 600; font-size: 15px; line-height: 1.2;
  }
  .slogan {
    font-family: "Lobster Two", "Brush Script MT", cursive;
    font-style: italic; font-weight: 700;
    color: var(--white); font-size: 36px; margin-left: 4px; line-height: 1;
  }

  .photo {
    position: absolute; left: 0; width: 100%;
    border-top: 3px solid var(--white); border-bottom: 3px solid var(--white);
  }
  .photo--day {
    top: 67px; height: 264px;
    background: linear-gradient(180deg, #eef3f8 0%, #dfe8f1 40%, #9fb6c9 56%, #5f7f8f 64%, #6d7a62 78%, #4f5b45 100%);
  }
  .photo--dusk {
    top: 67px; height: 176px;
    background: linear-gradient(180deg, #5d4d60 0%, #a66e6a 18%, #c9806f 32%, #463b4e 52%, #2c2b3d 75%, #3b3d52 100%);
  }
  .tagline {
    position: absolute; top: 98px; left: 0; width: 100%; text-align: center;
    color: var(--navy); font-weight: 600; font-size: 29px;
  }

  .message {
    position: absolute; left: 0; width: 100%;
    background: var(--navy); color: var(--white); text-align: center;
  }
  .card--front .message { top: 331px; height: 125px; padding: 16px 40px 0; font-size: 15.5px; line-height: 1.3; }
  .card--back .message { top: 243px; height: 190px; padding: 14px 30px 0; font-size: 14.6px; line-height: 1.05; }
  .message p + p { margin-top: 6px; }
  .message em { font-weight: 600; }

  .wave { position: absolute; left: 0; width: 703px; height: 60px; }
  .card--front .wave { top: 410px; }
  .card--back .wave { top: 395px; }

  .contact-row {
    position: absolute; left: 0; top: 457px; width: 100%; height: 46px;
  }
  .website {
    position: absolute; left: 23px; top: 13px;
    color: var(--navy); font-weight: 700; font-size: 18px;
  }
  .agents {
    position: absolute; left: 387px; top: 3px;
    display: grid; grid-template-columns: auto auto; column-gap: 9px; row-gap: 1px;
    font-size: 13px; line-height: 16px;
  }
  .agent-name { color: var(--navy); font-weight: 700; }
  .agent-email { color: var(--ink-grey); display: flex; align-items: center; gap: 5px; }
  .agent-email svg { width: 13px; height: 10px; }

  .partners {
    position: absolute; left: 22px; right: 22px; top: 443px;
    display: flex; justify-content: space-between;
  }
  .partner-badge { width: 48px; height: 48px; border-radius: 50%; border: 2px solid var(--badge-ring); }
  .partner-badge--lilac { background: #a896a6; }
  .partner-badge--green { background: #4e6a48; }
  .partner-badge--brown { background: #6b4a3a; }
  .partner-badge--black { background: #121212; }
  .partner-badge--blue { background: #3f7fb8; }
  .partner-badge--red { background: #d2262c; }
  .partner-badge--slate { background: #6d6f75; }
  .partner-badge--royal { background: #5b4fa0; }
  .partner-badge--pink { background: #e48ab8; }
</style>
</head>
<body>

<section class="card card--front">
  <header class="card__header">
    <div class="brand">Brindlemoor<br>Realty</div>
    <h1 class="slogan">Change Homes, Change Lives</h1>
  </header>
  <div class="photo photo--day" role="img" aria-label="Daytime view over a coastal town toward the beach, pier and ocean"></div>
  <h2 class="tagline">Changing the World One Home at a Time</h2>
  <div class="message">
    <p>Because we value generosity and desire to make a difference in our community and world, for every home bought or sold through us, we will make a contribution to one of our amazing partner who are helping to change the world.</p>
  </div>
  <svg class="wave" viewBox="0 0 703 60" preserveAspectRatio="none" aria-hidden="true">
    <path d="M0 0 H703 V22 C480 0 300 40 160 44 C90 46 40 36 0 18 Z" fill="var(--navy)"/>
    <path d="M0 18 C40 36 90 46 160 44 C300 40 480 0 703 22 V40 C500 20 330 50 170 54 C90 56 35 46 0 32 Z" fill="var(--sky-blue)"/>
    <path d="M0 32 C35 46 90 56 170 54 C330 50 500 20 703 40 V60 H0 Z" fill="var(--white)"/>
  </svg>
  <div class="contact-row">
    <div class="website">www.brindlemoorrealty.com</div>
    <div class="agents">
      <span class="agent-name">Evan Marlow</span>
      <span class="agent-email"><svg viewBox="0 0 13 10" aria-hidden="true"><rect x="0" y="0" width="13" height="10" fill="#6b7078"/><path d="M0.5 0.8 L6.5 5.5 L12.5 0.8" stroke="#fff" stroke-width="1" fill="none"/></svg>evan@brindlemoorrealty.com</span>
      <span class="agent-name">Jenna Marlow</span>
      <span class="agent-email"><svg viewBox="0 0 13 10" aria-hidden="true"><rect x="0" y="0" width="13" height="10" fill="#6b7078"/><path d="M0.5 0.8 L6.5 5.5 L12.5 0.8" stroke="#fff" stroke-width="1" fill="none"/></svg>jenna@brindlemoorrealty.com</span>
    </div>
  </div>
</section>

<section class="card card--back">
  <header class="card__header">
    <div class="brand">Brindlemoor<br>Realty</div>
    <h1 class="slogan">We live here.&nbsp; We give here.</h1>
  </header>
  <div class="photo photo--dusk" role="img" aria-label="Coastal town at dusk with city lights, pier and a pink sunset over the bay"></div>
  <div class="message">
    <p>We give because we value generosity and believe we have been blessed to be a blessing.<br>We believe that together we can change the world one home at time.</p>
    <p>You have our guarantee of personal service and no additional costs.&nbsp; The donations come out of our commission, not your pocket.&nbsp; You get to designate which of our amazing partner organizations you would like us to contribute to on behalf of your transaction.</p>
    <p>When you are ready to buy or sell, please consider giving us a call.&nbsp; Tell a friend about us too.<br><em>Together, we can make the world a better place.</em></p>
  </div>
  <svg class="wave" viewBox="0 0 703 60" preserveAspectRatio="none" aria-hidden="true">
    <path d="M0 0 H703 V22 C480 0 300 40 160 44 C90 46 40 36 0 18 Z" fill="var(--navy)"/>
    <path d="M0 18 C40 36 90 46 160 44 C300 40 480 0 703 22 V40 C500 20 330 50 170 54 C90 56 35 46 0 32 Z" fill="var(--sky-blue)"/>
    <path d="M0 32 C35 46 90 56 170 54 C330 50 500 20 703 40 V60 H0 Z" fill="var(--white)"/>
  </svg>
  <div class="partners" aria-label="Partner organizations">
    <span class="partner-badge partner-badge--lilac"></span>
    <span class="partner-badge partner-badge--green"></span>
    <span class="partner-badge partner-badge--brown"></span>
    <span class="partner-badge partner-badge--black"></span>
    <span class="partner-badge partner-badge--blue"></span>
    <span class="partner-badge partner-badge--red"></span>
    <span class="partner-badge partner-badge--slate"></span>
    <span class="partner-badge partner-badge--royal"></span>
    <span class="partner-badge partner-badge--pink"></span>
    <span class="partner-badge partner-badge--black"></span>
  </div>
</section>

</body>
</html>
```